A colourful crystal mystical tapestry

I need an image for my book cover. The title of the book is The Woven Lantern . Below, the subtitle is Along Quiet Rivers. The crystals move from bottom right to one third up the cover and into the middle. Stop below book title. (Book is 9x6). The crystals have to look like a multi-colour tapestry. Real crystals appear like they are gently exploding from the bottom right of the cover. More like movement than rocketships pls. But not a bunch of fragments. More clustered together. The upper cover will be white. They crystals are multi-covered bright - shinning. It can not be a bad AI image. It must be sharp and brilliant - a tapestry of colours. It is a spiritual book so, it needs to feel as such. If another creative idea comes to mind...give it a try.. I am open to something completely different as long as if is a multi-colour adult appealing spiritual unique image- which represents the title well. THANKS in advance.

Target Market(s)

Readers of multi-dimensional stories. ADULTS

Industry/Entity Type

Spirituality. Beautiful interesting intriguing.

Requirements
Nice to have
• It's tapestry, not chaos per say.
Should not have
• Anything crappy space like AI I can easily create. Be unique.

```html
<!DOCTYPE html>
<html lang="en">
<head>
<meta charset="utf-8">
<title>The Woven Lantern – Book Cover</title>
<link rel="stylesheet" href="https://fonts.googleapis.com/css2?family=Cinzel:wght@400;500;600;700&display=swap">
<style>
  :root {
    --page-bg: #f4f3f4;
    --cover-white: #ffffff;
    --ink: #111111;
    --rule: #3a3a3a;
    --crystal-magenta: #e0338f;
    --crystal-pink: #f26aa8;
    --crystal-orange: #f5873a;
    --crystal-gold: #f8c245;
    --crystal-blue: #2f6fd6;
    --crystal-cyan: #5fc6e4;
    --crystal-violet: #7a3fc4;
    --crystal-navy: #1d3566;
    --crystal-red: #d8242c;
  }
  * { margin: 0; padding: 0; box-sizing: border-box; }
  html, body {
    width: 1200px;
    height: 1200px;
    overflow: hidden;
    background: var(--page-bg);
  }
  .canvas {
    position: relative;
    width: 1200px;
    height: 1200px;
    display: flex;
    justify-content: center;
    align-items: center;
  }
  .cover {
    position: relative;
    width: 800px;
    height: 1200px;
    background: var(--cover-white);
    overflow: hidden;
    font-family: "Cinzel", "Trajan Pro", serif;
    color: var(--ink);
  }
  .title-lead {
    position: absolute;
    top: 72px;
    left: 0;
    width: 100%;
    display: flex;
    justify-content: center;
    align-items: center;
    gap: 22px;
  }
  .title-lead .rule {
    height: 1px;
    width: 166px;
    background: linear-gradient(90deg, transparent, var(--rule));
  }
  .title-lead .rule.right {
    width: 208px;
    background: linear-gradient(90deg, var(--rule), transparent);
  }
  .title-lead .word {
    font-size: 66px;
    font-weight: 500;
    line-height: 1;
    letter-spacing: 2px;
  }
  .title-main {
    position: absolute;
    top: 142px;
    left: 0;
    width: 100%;
    text-align: center;
    font-size: 136px;
    font-weight: 600;
    line-height: 1;
    letter-spacing: -2px;
    background: linear-gradient(100deg,
      var(--crystal-red) 0%, var(--crystal-orange) 18%, var(--crystal-pink) 34%,
      var(--crystal-magenta) 48%, var(--crystal-violet) 62%, var(--crystal-blue) 74%,
      var(--crystal-magenta) 88%, var(--crystal-red) 100%);
    -webkit-background-clip: text;
    background-clip: text;
    color: transparent;
  }
  .title-second {
    position: absolute;
    top: 268px;
    left: 0;
    width: 100%;
    text-align: center;
    font-size: 100px;
    font-weight: 500;
    line-height: 1;
    letter-spacing: 1px;
  }
  .subtitle {
    position: absolute;
    top: 378px;
    left: 0;
    width: 100%;
    text-align: center;
    font-size: 34px;
    font-weight: 500;
    line-height: 1;
    letter-spacing: 0;
  }
  .crystal-art {
    position: absolute;
    left: 200px;
    top: 390px;
    width: 600px;
    height: 810px;
    background:
      radial-gradient(ellipse 60% 45% at 85% 92%, var(--crystal-gold) 0%, var(--crystal-orange) 18%, transparent 48%),
      radial-gradient(ellipse 55% 40% at 55% 45%, var(--crystal-magenta) 0%, transparent 60%),
      radial-gradient(ellipse 50% 45% at 95% 45%, var(--crystal-cyan) 0%, transparent 62%),
      radial-gradient(ellipse 45% 35% at 30% 75%, var(--crystal-navy) 0%, var(--crystal-blue) 25%, transparent 65%),
      radial-gradient(ellipse 70% 55% at 80% 80%, var(--crystal-pink) 0%, var(--crystal-violet) 45%, transparent 75%),
      radial-gradient(ellipse 90% 85% at 100% 100%, rgba(242,106,168,0.55) 0%, rgba(95,198,228,0.35) 55%, transparent 80%);
    -webkit-mask-image: radial-gradient(ellipse 105% 95% at 100% 100%, #000 55%, transparent 80%);
    mask-image: radial-gradient(ellipse 105% 95% at 100% 100%, #000 55%, transparent 80%);
  }
  .author {
    position: absolute;
    left: 38px;
    top: 1138px;
    font-size: 34px;
    font-weight: 600;
    line-height: 1;
    letter-spacing: 0.5px;
  }
</style>
</head>
<body>
  <main class="canvas">
    <section class="cover">
      <div class="title-lead">
        <span class="rule left"></span>
        <span class="word">THE</span>
        <span class="rule right"></span>
      </div>
      <h1 class="title-main">WOVEN</h1>
      <div class="title-second">LANTERN</div>
      <p class="subtitle">ALONG QUIET RIVERS</p>
      <div class="crystal-art" role="img" aria-label="Illustration of brilliant multicoloured crystals in pink, blue, orange and violet bursting gently outward from the bottom right corner"></div>
      <p class="author">AUTHOR NAME</p>
    </section>
  </main>
</body>
</html>
```